Web design for an intellectual property law practice

I need to design a simple landing page that may in the future expand to a full site. It should be very high tech focused.

Target Market(s)

Anyone seeking legal services

Industry/Entity Type

Legal

Number of Pages Required

2 page

Font styles to use
Other font styles liked:
• The same font as my logo

Colors
ec1f27

Requirements
Must have
• My logo (see attached).
Nice to have
• Open to ideas.

```html
<!DOCTYPE html>
<html lang="en">
<head>
<meta charset="utf-8">
<title>northgate ip law</title>
<link rel="stylesheet" href="https://fonts.googleapis.com/css2?family=Montserrat:wght@400;600;700&family=Open+Sans:wght@400;600&family=Oswald:wght@300;400&display=swap">
<style>
:root{
  --red:#ec1f27;
  --ink:#222;
  --body:#666;
  --muted:#999;
  --light:#f2f2f2;
  --line:#e2e2e2;
  --dark:#2b2b2b;
  --darker:#1f1f1f;
  --white:#fff;
}
*{box-sizing:border-box;margin:0;padding:0}
html,body{width:1200px;height:4878px;overflow:hidden}
body{position:relative;background:var(--white);font-family:"Open Sans",Arial,sans-serif;color:var(--body);font-size:13px;line-height:1.7}
.abs{position:absolute}
.btn{position:absolute;display:inline-block;border:1.5px solid var(--red);border-radius:20px;color:var(--ink);font:600 11px/1 "Montserrat",Arial,sans-serif;letter-spacing:1.5px;text-transform:uppercase;padding:11px 26px;text-align:center;background:transparent}
.btn--light{color:var(--white)}
.btn--fill{background:var(--red);color:var(--white)}
.heading{font-family:"Montserrat",Arial,sans-serif;color:var(--ink)}

/* hero */
.hero{position:absolute;left:0;top:0;width:1200px;height:760px;background:linear-gradient(180deg,#fafafa 0%,#e7e7e7 45%,#cfcfcf 100%)}
.brand{position:absolute;left:88px;top:20px;text-align:center;width:110px}
.brand__dot{display:block;width:46px;height:46px;border:2px solid var(--ink);border-radius:50%;margin:0 auto 8px}
.brand__name{font:700 15px/1 "Montserrat",Arial,sans-serif;color:var(--ink)}
.topline{position:absolute;left:478px;top:44px;font-size:12px;color:var(--body)}
.topline b{font:600 18px/1 "Oswald",Arial,sans-serif;color:var(--red);margin-left:24px;vertical-align:-2px}
.topline + .btn{left:856px;top:38px;padding:10px 30px}
.nav{position:absolute;left:356px;top:116px;display:flex;gap:0;font:600 11px/1 "Montserrat",Arial,sans-serif;letter-spacing:1px;color:var(--ink)}
.nav span{margin-right:38px}
.nav .is-active{color:var(--red)}
.hero__title{position:absolute;left:0;width:1200px;top:248px;text-align:center;font:700 40px/1 "Montserrat",Arial,sans-serif;color:var(--ink)}
.hero__lead{position:absolute;left:400px;width:400px;top:300px;text-align:center;font-size:13px;color:#444;line-height:1.6}

/* welcome */
.welcome{position:absolute;left:0;top:550px;width:1200px;height:605px;background:linear-gradient(135deg,#383838,#1e1e1e);clip-path:polygon(0 150px,100% 0,100% 100%,0 100%)}
.welcome__eyebrow{position:absolute;left:172px;top:200px;font:600 14px/1 "Montserrat",Arial,sans-serif;letter-spacing:2px;color:var(--red)}
.welcome__title{position:absolute;left:172px;top:222px;font:700 30px/1 "Montserrat",Arial,sans-serif;color:var(--white)}
.welcome__text{position:absolute;left:172px;top:282px;width:520px;font-size:12.5px;color:#bbb;line-height:1.7}
.welcome__text p{margin-bottom:14px}
.stats{position:absolute;left:795px;top:150px;width:250px}
.stat{display:flex;align-items:center;height:150px;border-bottom:1px solid #555}
.stat:last-child{border-bottom:none}
.stat__num{font:300 62px/1 "Oswald",Arial,sans-serif;color:var(--red);width:88px}
.stat__label{font:600 14px/1.3 "Montserrat",Arial,sans-serif;color:var(--white)}

/* practice */
.section-title{position:absolute;left:0;width:1200px;text-align:center;font:400 28px/1 "Montserrat",Arial,sans-serif;color:var(--ink)}
.section-title b{font-weight:700}
.section-sub{position:absolute;left:350px;width:500px;text-align:center;font-size:12.5px;color:var(--body);line-height:1.6}
.card{position:absolute;top:1350px;width:234px;height:340px;background:var(--light);clip-path:polygon(0 0,100% 0,100% 86%,50% 100%,0 86%);text-align:center;padding-top:40px}
.card--active{background:var(--white);border-top:3px solid var(--red);box-shadow:0 0 20px rgba(0,0,0,.1);top:1340px;height:360px}
.card svg{width:40px;height:40px}
.card__title{font:700 15px/1 "Montserrat",Arial,sans-serif;color:var(--ink);margin:18px 0 14px}
.card__text{width:170px;margin:0 auto;font-size:12px;line-height:1.5}
.card .btn{position:static;margin-top:22px;padding:8px 28px}
.arrow{position:absolute;top:1500px;font:400 30px/1 "Open Sans",Arial,sans-serif;color:#bbb}
.scales{position:absolute;left:210px;top:1745px;width:780px;height:275px;background:radial-gradient(ellipse at 50% 60%,#6b4a36 0%,#a58a63 30%,#eeeeee 62%,#ffffff 80%)}
.available__pre{position:absolute;left:0;width:1200px;top:2083px;text-align:center;font-size:17px;color:#555}
.available__title{position:absolute;left:0;width:1200px;top:2118px;text-align:center;font:700 38px/1 "Montserrat",Arial,sans-serif;color:var(--ink)}

/* why */
.why{position:absolute;left:0;top:2309px;width:1200px;height:555px;background:var(--light)}
.why__photo{position:absolute;left:0;top:0;width:430px;height:555px;background:linear-gradient(135deg,#9c9c9c,#2f2f2f 55%,#111)}
.why__title{position:absolute;left:430px;width:770px;top:66px;text-align:center;font:700 29px/1 "Montserrat",Arial,sans-serif;color:var(--ink)}
.why__title span{color:#999;font-weight:400}
.why__sub{position:absolute;left:430px;width:770px;top:110px;text-align:center;font-size:12.5px}
.reason{position:absolute;width:300px;display:flex;gap:22px}
.reason__icon{flex:none;width:60px;height:60px;border-radius:50%;background:var(--white);display:flex;align-items:center;justify-content:center}
.reason--accent .reason__icon{background:var(--red)}
.reason__title{font:700 14px/1 "Montserrat",Arial,sans-serif;color:var(--ink);margin:4px 0 6px}
.reason__text{font-size:12px;line-height:1.5;width:150px}

/* profile */
.profile__name{position:absolute;left:172px;top:3022px;font:700 40px/1 "Montserrat",Arial,sans-serif;color:var(--ink)}
.profile__role{position:absolute;left:172px;top:3072px;font-size:13px;color:var(--ink)}
.profile__bio{position:absolute;left:172px;top:3115px;width:430px;font-size:12.5px;line-height:1.75}
.profile__photo{position:absolute;left:700px;top:2935px;width:420px;height:645px;background:linear-gradient(180deg,#f3f3f3 0%,#8a8f98 40%,#3d424b 100%);border-radius:180px 180px 0 0}

/* testimonial */
.testimonial{position:absolute;left:0;top:3400px;width:1200px;height:665px;background:linear-gradient(180deg,#e9e9e9,#f7f7f7 50%,#dcdcdc);clip-path:polygon(0 0,100% 150px,100% 100%,0 100%)}
.testimonial__avatar{position:absolute;left:560px;top:3640px;width:80px;height:80px;border-radius:50%;border:4px solid var(--white);background:linear-gradient(135deg,#e6c98f,#b3805d)}
.testimonial__quote{position:absolute;left:255px;width:690px;top:3745px;text-align:center;font-style:italic;font-size:14.5px;line-height:1.75;color:#555}
.testimonial__mark{position:absolute;left:0;width:1200px;top:3880px;text-align:center;font:700 22px/1 "Montserrat",Arial,sans-serif;color:var(--red)}
.testimonial__name{position:absolute;left:0;width:1200px;top:3908px;text-align:center;font:600 12px/1 "Montserrat",Arial,sans-serif;letter-spacing:2px;color:var(--ink)}
.testimonial__role{position:absolute;left:0;width:1200px;top:3928px;text-align:center;font-size:12px}
.dots{position:absolute;left:552px;top:3980px;display:flex;gap:10px}
.dots i{width:9px;height:9px;border-radius:50%;border:1.5px solid var(--red)}
.dots i:first-child{background:var(--red)}

/* cta */
.cta{position:absolute;left:0;top:4065px;width:1200px;height:180px;background:var(--red)}
.cta__title{position:absolute;left:172px;top:52px;font:700 29px/1.1 "Montserrat",Arial,sans-serif;color:var(--white)}
.cta__sub{position:absolute;left:172px;top:90px;font:400 17px/1 "Montserrat",Arial,sans-serif;color:var(--white)}
.cta .btn{left:772px;top:60px;border-color:var(--white);color:#7a0d11;width:260px}

/* contact */
.contact{position:absolute;left:0;top:4244px;width:602px;height:553px;background:linear-gradient(160deg,#2e2e2e,#1c1c1c)}
.contact__brand{position:absolute;left:172px;top:60px;font:700 19px/1 "Montserrat",Arial,sans-serif;color:var(--white)}
.contact__phone{position:absolute;left:172px;top:96px;font:400 28px/1 "Oswald",Arial,sans-serif;color:var(--white)}
.contact__phone b{color:var(--red);font-weight:400}
.contact__info{position:absolute;left:172px;top:140px;font-size:12.5px;color:#ccc;line-height:1.55}
.contact__info strong{display:block;color:var(--white);margin-top:16px;font-weight:600}
.contact .btn{left:172px;top:440px;color:var(--white)}
.booking{position:absolute;left:602px;top:4244px;width:598px;height:553px;background:var(--white)}
.booking__title{position:absolute;left:82px;top:60px;font:400 17px/1 "Montserrat",Arial,sans-serif;color:var(--ink)}
.booking__title b{font-weight:700}
.field{position:absolute;left:82px;width:345px;height:38px;border:1px solid var(--line);padding:9px 12px;font-size:11.5px;color:#aaa}
.booking .btn{left:82px;top:440px}

/* footer */
.footer{position:absolute;left:0;top:4797px;width:1200px;height:81px;background:#f5f5f5}
.footer__copy{position:absolute;left:172px;top:32px;font-size:11px;color:var(--muted)}
.social{position:absolute;left:902px;top:26px;display:flex;gap:10px}
.social i{width:30px;height:30px;border-radius:50%;background:#c4c4c4}
</style>
</head>
<body>

<header class="hero">
  <div class="hero" role="img" aria-label="Light grey photograph of classical courthouse columns" style="position:absolute;left:0;top:0"></div>
  <div class="brand"><span class="brand__dot"></span><span class="brand__name">northgate ip law</span></div>
  <div class="topline">Serving the State of New York<b>555.201.0700</b></div>
  <span class="btn">Get free consultation</span>
  <nav class="nav"><span class="is-active">PRACTICE AREAS</span><span>CASE RESULTS</span><span>LAWYERS</span><span>TESTIMONIALS</span><span>NEWS</span><span>FAQS</span><span>CONTACT</span></nav>
  <h1 class="hero__title">We fight for you</h1>
  <p class="hero__lead">At northgate ip law, justice is not an abstract term. It's something we create everyday for our clients.</p>
  <span class="btn" style="left:492px;top:380px">Contact us today!</span>
</header>

<section class="welcome" role="img" aria-label="Dark photograph of courthouse columns">
  <div class="welcome__eyebrow">WELCOME TO</div>
  <h2 class="welcome__title">northgate ip law</h2>
  <div class="welcome__text">
    <p>We practice in personal injury, family, criminal and labor litigation, with an emphasis on complex contractual matters and mass tort litigation. We are a leading group of highly professional lawyers whose goal is to protect you, your family and business.</p>
    <p>We aim to assure our clients that with our help it is possible to quickly and effectively resolve any issue. We are a leading group of highly professional lawyers ...</p>
  </div>
  <span class="btn btn--light" style="left:172px;top:508px">More about us</span>
  <div class="stats">
    <div class="stat"><span class="stat__num">15</span><span class="stat__label">Years<br>of Experience</span></div>
    <div class="stat"><span class="stat__num">23</span><span class="stat__label">Professional<br>Attorneys</span></div>
    <div class="stat"><span class="stat__num">64</span><span class="stat__label">New Cases<br>in Year</span></div>
  </div>
</section>

<section class="practice">
  <h2 class="section-title" style="top:1222px">Practice <b>Areas</b></h2>
  <p class="section-sub" style="top:1260px">Lorem ipsum dolor sit amet, consectetur adipiscing elit, sed do eiusmod tempor incididunt ut labore et dolore.</p>
  <span class="arrow" style="left:36px">‹</span><span class="arrow" style="left:1148px">›</span>
  <article class="card" style="left:88px">
    <svg viewBox="0 0 40 40" fill="none" stroke="#ec1f27" stroke-width="3"><circle cx="12" cy="24" r="8"/><circle cx="28" cy="24" r="8"/><path d="M16 14h8"/></svg>
    <h3 class="card__title">Criminal Law</h3>
    <p class="card__text">Lorem ipsum dolor sit amet, consectetur adipiscing elit, sed do eiusmod tempor incididunt</p>
    <span class="btn">More</span>
  </article>
  <article class="card card--active" style="left:351px">
    <svg viewBox="0 0 40 40" fill="#ec1f27"><rect x="4" y="12" width="32" height="22" rx="2"/><path d="M14 12V7h12v5h-3V10h-6v2z"/></svg>
    <h3 class="card__title">Business Law</h3>
    <p class="card__text">Lorem ipsum dolor sit amet, consectetur adipiscing elit, sed do eiusmod tempor incididunt</p>
    <span class="btn btn--fill">More</span>
  </article>
  <article class="card" style="left:618px">
    <svg viewBox="0 0 40 40" fill="none" stroke="#ec1f27" stroke-width="3"><rect x="5" y="5" width="30" height="30" rx="2"/><circle cx="20" cy="20" r="6"/></svg>
    <h3 class="card__title">Finance Law</h3>
    <p class="card__text">Lorem ipsum dolor sit amet, consectetur adipiscing elit, sed do eiusmod tempor incididunt</p>
    <span class="btn">More</span>
  </article>
  <article class="card" style="left:881px">
    <svg viewBox="0 0 40 40" fill="none" stroke="#ec1f27" stroke-width="3"><path d="M8 4h18l6 6v26H8z"/><path d="M14 16h12M14 22h12M14 28h8"/></svg>
    <h3 class="card__title">Insurance Law</h3>
    <p class="card__text">Lorem ipsum dolor sit amet, consectetur adipiscing elit, sed do eiusmod tempor incididunt</p>
    <span class="btn">More</span>
  </article>
  <div class="scales" role="img" aria-label="Scales of justice, open book and gavel"></div>
  <p class="available__pre">If you have any legal problem in your Life</p>
  <h2 class="available__title">we are available</h2>
  <span class="btn" style="left:470px;top:2200px;width:260px">Get free consultation</span>
</section>

<section class="why">
  <div class="why__photo" role="img" aria-label="Lawyer holding a document beside a gavel"></div>
  <h2 class="why__title">Why <span>Choose Us?</span></h2>
  <p class="why__sub">We have 15 years of experience and Customer satisfaction with:</p>
  <div class="reason reason--accent" style="left:510px;top:160px">
    <span class="reason__icon"><svg width="24" height="24" viewBox="0 0 24 24" fill="none" stroke="#fff" stroke-width="2"><path d="M12 2l3 7 7 .6-5.4 4.7 1.7 7.2L12 17.6 5.7 21.5l1.7-7.2L2 9.6 9 9z"/></svg></span>
    <div><h3 class="reason__title">Trusted</h3><p class="reason__text">Lorem ipsum dolor sit amet, consectetur adipiscing elit, sed do eiusmod tempor ...</p></div>
  </div>
  <div class="reason" style="left:852px;top:160px">
    <span class="reason__icon"><svg width="24" height="24" viewBox="0 0 24 24" fill="none" stroke="#ec1f27" stroke-width="2"><path d="M6 3h12v5a6 6 0 0 1-12 0z"/><path d="M12 14v4M8 21h8"/></svg></span>
    <div><h3 class="reason__title">Experience</h3><p class="reason__text">Lorem ipsum dolor sit amet, consectetur adipiscing elit, sed do eiusmod tempor ...</p></div>
  </div>
  <div class="reason" style="left:510px;top:290px">
    <span class="reason__icon"><svg width="24" height="24" viewBox="0 0 24 24" fill="none" stroke="#ec1f27" stroke-width="2"><path d="M4 20l9-9M11 5l8 8M14 2l8 8"/></svg></span>
    <div><h3 class="reason__title">Legal</h3><p class="reason__text">Lorem ipsum dolor sit amet, consectetur adipiscing elit, sed do eiusmod tempor ...</p></div>
  </div>
  <div class="reason" style="left:852px;top:290px">
    <span class="reason__icon"><svg width="24" height="24" viewBox="0 0 24 24" fill="none" stroke="#ec1f27" stroke-width="2"><rect x="2" y="6" width="20" height="12" rx="2"/><circle cx="12" cy="12" r="3"/></svg></span>
    <div><h3 class="reason__title">Low Cost</h3><p class="reason__text">Lorem ipsum dolor sit amet, consectetur adipiscing elit, sed do eiusmod tempor ...</p></div>
  </div>
  <span class="btn" style="left:708px;top:458px">Contact us today!</span>
</section>

<section class="profile">
  <h2 class="profile__name">Daniel Marsh</h2>
  <p class="profile__role">Business &amp; Finance Lawyer</p>
  <p class="profile__bio">Lorem ipsum dolor sit amet, consectetur adipiscing elit, sed do eiusmod tempor incididunt ut labore et dolore magna aliqua. Ut enim ad minim veniam, quis nostrud exercitation ullamco laboris nisi ut aliquip ex ea commodo consequat. Duis aute irure dolor in reprehenderit.</p>
  <span class="btn" style="left:172px;top:3266px">More</span>
  <div class="profile__photo" role="img" aria-label="Portrait of the lawyer in a grey suit"></div>
</section>

<section class="testimonial" role="img" aria-label="Light photograph of courthouse columns"></section>
<div class="testimonial__avatar" role="img" aria-label="Client portrait"></div>
<p class="testimonial__quote">Lorem ipsum dolor sit amet, consectetur adipiscing elit, sed do eiusmod tempor incididunt ut labore et dolore magna aliqua. Ut enim ad minim veniam, quis nostrud exercitation ullamco laboris nisi ut aliquip ex ea commodo consequat. Duis aute irure dolor in reprehenderit.</p>
<div class="testimonial__mark">“</div>
<div class="testimonial__name">- CLARA WHITMORE -</div>
<div class="testimonial__role">Business &amp; Finance</div>
<div class="dots"><i></i><i></i><i></i><i></i><i></i></div>

<section class="cta">
  <h2 class="cta__title">Are you having any problems</h2>
  <p class="cta__sub">but can't consult to anyone?</p>
  <span class="btn">Contact us today!</span>
</section>

<section class="contact" role="img" aria-label="Dark photograph of a justice statue">
  <div class="contact__brand">northgate ip law</div>
  <div class="contact__phone">Call : <b>+1 555-014-2235</b></div>
  <div class="contact__info">
    e: hello@northgate.example
    <strong>Address:</strong>42, Linden Ave. Northwest<br>Washington, DC 0000
    <strong>Office Hours:</strong>Monday to Saturday<br>9:00 - 18:00<br>Sunday: Closed
  </div>
  <span class="btn">Contact us</span>
</section>

<section class="booking">
  <h2 class="booking__title"><b>Book</b> Free consultation</h2>
  <div class="field" style="top:100px">Your Name</div>
  <div class="field" style="top:150px">Email</div>
  <div class="field" style="top:200px">Phone</div>
  <div class="field" style="top:250px;height:150px">Message...</div>
  <span class="btn">Contact us</span>
</section>

<footer class="footer">
  <p class="footer__copy">© Copyright 2019 northgate ip law</p>
  <div class="social"><i></i><i></i><i></i><i></i><i></i></div>
</footer>

</body>
</html>
```